Design and Renovation Company Luxury Business Card

I want to create a luxury business card for a Design and Renovation Firm . We will use our current logo. The company name is 742BUILD. We do not want anything standard. We need a very unique concept.
Please see uploaded inspiration. I really like the textured paper option. I would like the card to be thick with debossing, and/or embossing options. The logo has orange in it but I would like to see the card with and without the orange. I think the orange may make the company feel less high-end. The goal is to elevate the logo not match its vibe per se of the logo. We want something very unique, not standard at all!
I would like a space for :
Logo,
Name,
Position,
Email,
Office number,
Website Address,
Business Address,
Thank you!
Have fun!
Target Market(s)
Home owners Age 35 +
Industry/Entity Type
Design and Renovation
Contact Information for Business Card
Logo, Name, Position, Email, Office number, Website Address, Business Address,.
Colors
Designer to choose colors to be used in the design.
Requirements
Must have
- A luxury designer feel. Must be black or dark grey but open to other luxury ideas.
Nice to have
- Gold, silver, black embossing or debossing. Textured paper design.
Should not have
- A cheap look and feel.

```html
<!DOCTYPE html>
<html lang="fr">
<head>
<meta charset="utf-8">
<title>742BUILD – Carte de visite</title>
<link rel="stylesheet" href="https://fonts.googleapis.com/css2?family=Barlow:ital,wght@0,400;0,500;0,600;1,400&display=swap">
<style>
  :root {
    --backdrop: #d9dadb;
    --card: #0e1013;
    --card-glow: #15171b;
    --ink-white: #ffffff;
    --accent: #f39a1f;
    --texture: rgba(60, 62, 68, 0.35);
  }
  * { margin: 0; padding: 0; box-sizing: border-box; }
  html, body {
    width: 807px; height: 1200px; overflow: hidden;
    background: var(--backdrop);
    font-family: "Barlow", "Helvetica Neue", Arial, sans-serif;
  }
  .stage { position: relative; width: 807px; height: 1200px; }
  .card {
    position: absolute; left: 53px; width: 702px; height: 421px;
    background: radial-gradient(ellipse 60% 55% at 50% 30%, var(--card-glow), var(--card) 70%);
    box-shadow: 0 8px 18px rgba(0,0,0,0.25);
    overflow: hidden;
  }
  .card--front { top: 168px; }
  .card--back { top: 635px; }
  .card__texture {
    position: absolute; left: 0; right: 0; bottom: 0; height: 45%;
    background: linear-gradient(to bottom, transparent, var(--texture));
  }

  /* front */
  .brand-mark {
    position: absolute; left: 332px; top: 306px; width: 57px; height: 57px;
    background: var(--ink-white);
  }
  .brand-name {
    position: absolute; left: 399px; top: 296px;
    font-size: 56px; font-weight: 500; line-height: 1;
    letter-spacing: 3px; color: var(--ink-white); white-space: nowrap;
  }
  .brand-tagline {
    position: absolute; left: 403px; top: 353px;
    font-size: 13px; font-weight: 600; line-height: 1;
    letter-spacing: 4.1px; color: var(--ink-white); white-space: nowrap;
  }

  /* back */
  .holder {
    position: absolute; left: 0; right: 0; top: 82px; text-align: center;
  }
  .holder__name {
    font-size: 31px; font-weight: 600; line-height: 1;
    letter-spacing: 1px; color: var(--ink-white);
  }
  .holder__role {
    margin-top: 3px; font-size: 15px; font-style: italic; font-weight: 400;
    line-height: 1.1; color: var(--accent); letter-spacing: 0.3px;
  }
  .rule {
    position: absolute; top: 225px; height: 2px; background: var(--ink-white);
  }
  .rule--left { left: 51px; width: 251px; }
  .rule--right { left: 404px; width: 247px; }
  .badge-mark {
    position: absolute; left: 329px; top: 183px; width: 44px; height: 44px;
    background: var(--ink-white);
  }
  .badge-name {
    position: absolute; left: 0; right: 0; top: 229px; text-align: center;
    font-size: 10px; font-weight: 600; letter-spacing: 1px; color: var(--ink-white);
  }
  .credentials, .contact {
    position: absolute; font-size: 14.5px; color: var(--accent); letter-spacing: 0.4px;
    white-space: nowrap;
  }
  .credentials { right: 400px; top: 258px; text-align: right; line-height: 20.6px; }
  .contact { left: 404px; top: 256px; line-height: 17px; }
</style>
</head>
<body>
<main class="stage">
  <section class="card card--front" aria-label="Recto">
    <div class="card__texture" role="img" aria-label="Faint dotted wave texture"></div>
    <div class="brand-mark"></div>
    <div class="brand-name">742BUILD</div>
    <div class="brand-tagline">Design and Renovation Firm</div>
  </section>

  <section class="card card--back" aria-label="Verso">
    <div class="card__texture" role="img" aria-label="Faint dotted wave texture"></div>
    <div class="holder">
      <h1 class="holder__name">MARC VELLAN</h1>
      <p class="holder__role">DIRECTEUR FONDATEUR</p>
    </div>
    <div class="rule rule--left"></div>
    <div class="badge-mark"></div>
    <div class="badge-name">742BUILD</div>
    <div class="rule rule--right"></div>
    <div class="credentials">
      Certifié ZRT et Velmocert<br>
      Registre KOVALT no 51726<br>
      Mandataire Fiscal no K70215
    </div>
    <div class="contact">
      +12 (0) 98 765 43 2<br>
      marc.vellan@742build.ch
    </div>
  </section>
</main>
</body>
</html>
```